Win a Korvane Tillman Iron Mule

I need a billboard that grabs peoples attention. It only going to be up for 100 days

Target Market(s)

People who want to refresh their Benchmark 42 or Supervisor K478 Competencies

Industry/Entity Type

Mining

Colors
0054AA
0677BA
7BADD7
CADEEF
E8F1F8
FFF300
FFF600
FEFA6F
FFFEC7
FFFEE8

Requirements
Nice to have
• Picture of a the Korvane Motorbike and my logo

```html
<!DOCTYPE html>
<html lang="en">
<head>
<meta charset="utf-8">
<title>Redgum Operator Training Billboard</title>
<link rel="stylesheet" href="https://fonts.googleapis.com/css2?family=Montserrat:wght@800&display=swap">
<style>
  :root {
    --page-bg: #e8f1f8;
    --board-bg: #ffffff;
    --navy: #0b2a66;
    --blue: #0054aa;
    --yellow: #f6c400;
    --ink: #0a0a0a;
    --photo-sky: #7badd7;
    --photo-hill: #3f6b52;
    --photo-road: #b9bdc0;
  }
  html, body {
    margin: 0;
    width: 1200px;
    height: 1200px;
    overflow: hidden;
    background: var(--page-bg);
  }
  .canvas {
    position: relative;
    width: 1200px;
    height: 1200px;
    display: flex;
    align-items: center;
    justify-content: center;
  }
  .billboard {
    position: relative;
    width: 1120px;
    height: 350px;
    background: var(--board-bg);
    overflow: hidden;
    box-shadow: 0 6px 24px rgba(0, 0, 0, 0.18);
  }
  .billboard__photo {
    position: absolute;
    left: 0;
    top: 0;
    width: 440px;
    height: 350px;
  }
  .brand-rule {
    position: absolute;
    height: 6px;
  }
  .brand-rule--top {
    left: 570px;
    top: 62px;
    width: 500px;
    background: var(--navy);
  }
  .brand-rule--bottom {
    left: 570px;
    top: 188px;
    width: 500px;
    background: var(--yellow);
  }
  .brand {
    position: absolute;
    left: 455px;
    top: 62px;
    width: 620px;
    height: 132px;
    display: flex;
    align-items: center;
  }
  .brand__dot {
    width: 92px;
    height: 92px;
    border-radius: 50%;
    background: var(--blue);
    flex: none;
  }
  .brand__name {
    margin-left: 40px;
    font-family: "Montserrat", sans-serif;
    font-weight: 800;
    color: var(--ink);
    line-height: 1;
    text-transform: uppercase;
  }
  .brand__name-main {
    display: block;
    font-size: 62px;
    letter-spacing: 3px;
  }
  .brand__name-sub {
    display: block;
    margin-top: 10px;
    font-size: 24px;
    letter-spacing: 1.5px;
  }
  .contact {
    position: absolute;
    left: 470px;
    top: 226px;
    width: 610px;
    display: flex;
    align-items: center;
  }
  .contact__icon {
    width: 54px;
    height: 54px;
    flex: none;
  }
  .contact__number {
    margin-left: 16px;
    font-family: "Montserrat", sans-serif;
    font-weight: 800;
    font-size: 70px;
    letter-spacing: 0;
    color: var(--ink);
    line-height: 1;
    white-space: nowrap;
  }
</style>
</head>
<body>
  <main class="canvas">
    <section class="billboard">
      <svg class="billboard__photo" viewBox="0 0 440 350" role="img" aria-label="Photo of the Korvane Tillman Iron Mule motorbike parked on a lakeside road with forested hills behind">
        <defs>
          <linearGradient id="photoTones" x1="0" y1="0" x2="0" y2="1">
            <stop offset="0" stop-color="var(--photo-sky)"/>
            <stop offset="0.45" stop-color="var(--photo-hill)"/>
            <stop offset="0.75" stop-color="#5e6a6e"/>
            <stop offset="1" stop-color="var(--photo-road)"/>
          </linearGradient>
        </defs>
        <polygon points="0,0 300,0 410,350 0,350" fill="url(#photoTones)"/>
        <polygon points="300,0 312,0 422,350 410,350" fill="var(--navy)"/>
      </svg>

      <div class="brand-rule brand-rule--top"></div>
      <div class="brand">
        <span class="brand__dot"></span>
        <div class="brand__name">
          <span class="brand__name-main">Redgum</span>
          <span class="brand__name-sub">Operator Training</span>
        </div>
      </div>
      <div class="brand-rule brand-rule--bottom"></div>

      <div class="contact">
        <svg class="contact__icon" viewBox="0 0 54 54" aria-hidden="true">
          <circle cx="27" cy="27" r="26" fill="var(--navy)"/>
          <circle cx="27" cy="27" r="22" fill="var(--yellow)"/>
          <path d="M18 15c2-1 4 0 5 2l2 4c1 2 0 3-1 4l-1 1c1 3 4 6 7 7l1-1c1-1 2-2 4-1l4 2c2 1 3 3 2 5l-1 2c-1 2-4 3-7 2-8-3-14-9-17-17-1-3 0-6 2-7z" fill="var(--navy)"/>
          <path d="M31 14a10 10 0 0 1 9 9M31 19a5 5 0 0 1 4 4" fill="none" stroke="var(--navy)" stroke-width="2.2" stroke-linecap="round"/>
        </svg>
        <span class="contact__number">555.204.6183</span>
      </div>
    </section>
  </main>
</body>
</html>
```